Lumora business card for a plastic surgeon

we need a business card for plastic surgeons that work on a clinic called LUMORA.
we want a clean design and the following informations: name of the doctor, doctor's registration number (called CRM), telephone, address, facebook, instagram.
Colors: white, blue tones, light brown/ coffee

facebook and instagram: lumoraesteticaclinica

Industry/Entity Type

Business

Contact Information for Business Card

clean design

Font styles to use
Serif
Sans Serif
Other font styles liked:
• helvetica light

Colors
cee9f5
85cae6
85abd2
3276b5
cfeae6
cedeed
eaf1f7

Requirements
Must have
• doctor's name
• identification number (called CRM)
• contact (phone, facebook, instagram, address)

```html
<!DOCTYPE html>
<html lang="pt">
<head>
<meta charset="utf-8">
<title>Lumora – Business Card</title>
<link href="https://fonts.googleapis.com/css2?family=Cinzel:wght@400&family=Open+Sans:wght@400&display=swap" rel="stylesheet">
<style>
  :root {
    --stage: #5b5859;
    --coffee: #ac9280;
    --paper: #ffffff;
    --aqua: #05c6e0;
    --aqua-text: #3fd0e6;
    --slate: #4a6a85;
    --navy: #17385f;
    --ink: #1a1a1a;
  }
  * { margin: 0; padding: 0; box-sizing: border-box; }
  html, body { width: 1200px; height: 987px; overflow: hidden; background: var(--stage); }
  .stage { position: relative; width: 1200px; height: 987px; }

  .card { position: absolute; top: 33px; width: 509px; height: 888px; overflow: hidden; }
  .card--front { left: 43px; background: var(--coffee); }
  .card--back { left: 625px; background: var(--paper); }

  .serif { font-family: "Cinzel", "Times New Roman", serif; }
  .sans { font-family: "Open Sans", "Helvetica Neue", Arial, sans-serif; }

  /* Front */
  .front-mark {
    position: absolute; left: 123px; top: 192px;
    width: 260px; height: 260px; border-radius: 50%; background: var(--aqua);
  }
  .front-wordmark {
    position: absolute; left: 0; width: 100%; top: 478px; text-align: center;
    font-size: 92px; line-height: 1; color: var(--aqua-text); letter-spacing: 2px;
  }
  .front-tagline {
    position: absolute; left: 0; width: 100%; top: 592px; text-align: center;
    font-size: 35px; line-height: 1; color: var(--paper); letter-spacing: 1px;
  }

  /* Back */
  .back-wordmark {
    position: absolute; left: 0; width: 100%; top: 108px; text-align: center;
    font-size: 86px; line-height: 1; color: var(--aqua-text); letter-spacing: 2px;
  }
  .back-tagline {
    position: absolute; left: 0; width: 100%; top: 206px; text-align: center;
    font-size: 33px; line-height: 1; color: var(--slate); letter-spacing: 1px;
  }
  .doctor-name {
    position: absolute; left: 78px; top: 286px;
    font-size: 52px; line-height: 1; color: var(--aqua); letter-spacing: 0.5px;
  }
  .doctor-crm {
    position: absolute; left: 78px; top: 352px;
    font-size: 28px; line-height: 1; color: var(--navy);
  }
  .contact { position: absolute; left: 72px; display: flex; align-items: center; gap: 8px; }
  .contact--address { top: 435px; }
  .contact--phone { top: 523px; }
  .contact--social { top: 592px; }
  .contact__icon { width: 44px; height: 44px; flex: none; }
  .contact__text { font-size: 23px; line-height: 34px; color: var(--ink); }

  .back-band { position: absolute; left: 0; top: 0; width: 509px; height: 888px; }
</style>
</head>
<body>
<main class="stage">

  <section class="card card--front">
    <div class="front-mark"></div>
    <div class="front-wordmark serif">LUMORA</div>
    <div class="front-tagline serif">CIRURGIA PLÁSTICA</div>
  </section>

  <section class="card card--back">
    <svg class="back-band" viewBox="0 0 509 888" aria-hidden="true">
      <path d="M0 705 Q 260 815 509 707 L509 888 L0 888 Z" fill="var(--coffee)"/>
      <circle cx="415" cy="822" r="44" fill="var(--aqua)"/>
    </svg>

    <div class="back-wordmark serif">LUMORA</div>
    <div class="back-tagline serif">CIRURGIA PLÁSTICA</div>

    <div class="doctor-name sans">NAME HERE</div>
    <div class="doctor-crm sans">CRM 121212</div>

    <div class="contact contact--address">
      <svg class="contact__icon" viewBox="0 0 44 44" aria-hidden="true">
        <rect width="44" height="44" rx="6" fill="var(--aqua)"/>
        <path d="M22 8c-6 0-10.5 4.5-10.5 10.3C11.5 26 22 37 22 37s10.5-11 10.5-18.7C32.5 12.5 28 8 22 8z" fill="#fff"/>
        <circle cx="22" cy="18.5" r="4.2" fill="var(--aqua)"/>
      </svg>
      <div class="contact__text sans">8630 abcdeford Rd. Suite 154<br>your city, mnopqurs 21046</div>
    </div>

    <div class="contact contact--phone">
      <svg class="contact__icon" viewBox="0 0 44 44" aria-hidden="true">
        <rect width="44" height="44" rx="6" fill="var(--aqua)"/>
        <path d="M14 9l5 1 2 7-3 2c1.5 4 4 6.7 7.5 8.5l2.3-2.8 7 2 .7 5.3c-1 2-3 3-5 3C20 34 10 24 10 14c0-2 1.5-4.3 4-5z" fill="#fff"/>
      </svg>
      <div class="contact__text sans" style="line-height:28px">000.1234.5678<br>000.1234.2564</div>
    </div>

    <div class="contact contact--social">
      <svg class="contact__icon" viewBox="0 0 44 44" aria-hidden="true">
        <rect width="44" height="44" rx="6" fill="var(--aqua)"/>
        <circle cx="22" cy="22" r="14" fill="none" stroke="#fff" stroke-width="2.5"/>
        <ellipse cx="22" cy="22" rx="6" ry="14" fill="none" stroke="#fff" stroke-width="2"/>
        <line x1="8" y1="22" x2="36" y2="22" stroke="#fff" stroke-width="2"/>
        <line x1="10" y1="15" x2="34" y2="15" stroke="#fff" stroke-width="1.6"/>
        <line x1="10" y1="29" x2="34" y2="29" stroke="#fff" stroke-width="1.6"/>
      </svg>
      <div class="contact__text sans" style="line-height:28px">lumoraesteticaclinica<br>lumoraesteticaclinica</div>
    </div>
  </section>

</main>
</body>
</html>
```